Modern Venture Capital website

Design a modern website for a venture capital firm. This website should be modern and beautiful and be on par with other Venture Capital websites. I have a logo and a hero video I'd like to use. Link to hero video: https://files.vantoria.example/f/9Xk2Lm7qPz4Rt8Wb3Nc6Hd5Jy1Gs0Ve/view?ref=share_link

Preference will be given to the best design that combines design with the best images and digital content. That means no generic free stock videos 😅

I currently built a wix website to give you an idea of what content needs to be on the website. Depending on your design it can be 3 pages, or one long page. I will leave it up to you.

WEBSITE: https://brelmor58204.pagecraftly.example/my-site-4

Target Market(s)

Mid-career professionals, individuals interested in Venture Capital

Industry/Entity Type

Finance, venture capital, startups

Requirements
Must have
• must use the hero video I have and must use my logo. Must use high quality images that matches the website design - no generic stock images

```html
<!DOCTYPE html>
<html lang="en">
<head>
<meta charset="utf-8">
<title>Duskfall Ventures</title>
<link href="https://fonts.googleapis.com/css2?family=Montserrat:wght@300;400;500;600;700;800&display=swap" rel="stylesheet">
<style>
:root{
  --orange:#ff5a1f;
  --orange-soft:#f26a34;
  --black:#000;
  --ink:#111;
  --grey-text:#6b6b6b;
  --grey-band:#b8b8b8;
  --card-grey:#d9d9d9;
  --white:#fff;
}
*{box-sizing:border-box;margin:0;padding:0}
html,body{width:1200px;height:3993px;overflow:hidden}
body{position:relative;background:var(--white);font-family:'Montserrat',sans-serif;color:var(--ink)}
.abs{position:absolute}
.btn{position:absolute;display:flex;align-items:center;justify-content:center;gap:10px;border-radius:30px;font-weight:600;font-size:15px;color:var(--white);background:var(--orange)}
.btn svg{width:22px;height:10px}

/* hero */
.hero-bg{left:0;top:0;width:1200px;height:720px;background:
  radial-gradient(ellipse 60% 25% at 60% 75%,rgba(255,150,60,.35),transparent 70%),
  linear-gradient(180deg,#020202 0%,#0b0a08 45%,#2a1d10 80%,#3b2614 100%)}
.hero-curve{left:0;top:0;width:1200px;height:720px}
.logo{display:flex;flex-direction:column;color:var(--white);line-height:1}
.logo .name{font-weight:800;font-size:46px;letter-spacing:-1px}
.logo .sub{font-weight:700;font-size:15px;letter-spacing:5px;margin-top:-2px}
.nav{top:42px;left:598px;display:flex;gap:0;font-size:17px;color:var(--white)}
.nav a{position:absolute;white-space:nowrap;color:var(--white);text-decoration:none}
.nav .active{color:var(--orange)}
.user{left:1045px;top:33px;width:43px;height:43px;border-radius:50%;background:var(--white)}
.hero-title{left:113px;top:184px;font-size:50px;font-weight:500;color:var(--white);line-height:64px}
.hero-title em{font-style:normal;color:var(--orange)}
.hero-sub{left:116px;top:333px;font-size:23px;font-weight:700;color:var(--white)}
.hero-moon{left:690px;top:132px;width:122px;height:122px;border-radius:50%;background:radial-gradient(circle at 40% 40%,#e8dcc0,#a89877 70%,#6d624c)}
.scroll-dot{left:565px;top:658px;width:70px;height:70px;border-radius:50%;background:var(--white);box-shadow:0 2px 8px rgba(0,0,0,.25)}

/* headings */
.sec-title{position:absolute;left:0;width:1200px;text-align:center;font-size:44px;font-weight:300;color:var(--ink)}
.sec-title b{font-weight:700}
.divider{position:absolute;height:14px}
.divider i{position:absolute;top:6px;height:2px;width:85px;background:var(--orange)}
.divider span{position:absolute;top:0;width:14px;height:14px;border-radius:50%;border:2px solid #aaa}

/* about */
.moon-big{left:107px;top:871px;width:490px;height:490px;border-radius:50%;background:radial-gradient(circle at 45% 40%,#d7d7d7,#8a8a8a 60%,#4a4a4a)}
.about-title{left:651px;top:836px;font-size:44px;font-weight:300;line-height:56px}
.about-title b{font-weight:700}
.about-text{left:651px;top:1012px;width:436px;font-size:17px;line-height:26.5px;color:var(--grey-text);font-weight:400}
.about-text p+p{margin-top:27px}

/* fund */
.stat{position:absolute;top:1623px;width:185px;height:195px;background:var(--white);border-radius:8px;box-shadow:0 2px 10px rgba(0,0,0,.15);text-align:center}
.stat .num{margin-top:28px;font-size:50px;font-weight:700;color:var(--orange)}
.stat hr{width:120px;margin:8px auto 0;border:0;border-top:1px solid #ccc}
.stat .lab{margin-top:22px;font-size:17px;line-height:26px;color:#333}

/* become */
.vc-band{left:0;top:1927px;width:1200px;height:697px;background:radial-gradient(ellipse at 30% 30%,#2c2c2c,#0e0e0e 70%)}
.vc-title{color:var(--white)}
.vc-lead{left:0;top:2135px;width:1200px;text-align:center;font-size:16.5px;line-height:30px;color:var(--white)}
.vc-card{position:absolute;top:2237px;width:314px;height:476px;border-radius:4px 4px 160px 160px;background:var(--card-grey);text-align:center}
.vc-card.dark{background:var(--black);color:var(--white)}
.vc-card .img{margin:10px 10px 0;height:194px}
.vc-card h3{margin:28px auto 0;width:290px;font-size:22px;font-weight:600;line-height:30px}
.vc-card p{margin:26px auto 0;width:230px;font-size:15.5px;line-height:26.5px}
.vc-card .go{position:absolute;left:137px;top:418px;width:40px;height:40px}
.slide-arrow{position:absolute;top:2423px;width:42px;height:42px}

/* partners */
.partner{position:absolute;top:2964px;width:231px;height:125px;border-radius:12px;background:var(--black);box-shadow:0 2px 8px rgba(0,0,0,.2)}
.partner span{position:absolute;left:70px;top:52px;width:91px;height:22px;border-radius:4px;background:#3a3a3a}

/* cta + footer */
.foot-curve{left:0;top:3100px;width:1200px;height:893px}
.cta{left:107px;top:3221px;width:979px;height:318px;border-radius:160px;background:var(--orange-soft)}
.cta-title{left:0;top:3276px;width:1200px;text-align:center;font-size:44px;font-weight:300;color:var(--white)}
.cta-title b{font-weight:700}
.cta-text{left:0;top:3404px;width:1200px;text-align:center;font-size:17px;font-weight:600;color:var(--white)}
.foot-h{font-size:22px;font-weight:600;color:var(--white)}
.foot-line{height:2px;width:50px;background:var(--orange)}
.foot-txt{font-size:16px;line-height:26px;color:var(--white)}
.social{position:absolute;top:3813px;width:32px;height:32px;border-radius:50%;border:1.5px solid var(--white)}
.input{left:724px;top:3751px;width:338px;height:53px;background:var(--white);border-radius:4px}
.check{left:727px;top:3833px;width:22px;height:22px;border:2px solid var(--white);border-radius:2px}
.copy{left:0;top:3921px;width:1200px;text-align:center;font-size:15px;font-weight:600;color:var(--white)}
</style>
</head>
<body>

<!-- HERO -->
<div class="abs hero-bg" role="img" aria-label="Night skyline video of a downtown city with lit towers"></div>
<svg class="abs hero-curve" viewBox="0 0 1200 720" aria-hidden="true">
  <path d="M0,555 Q600,785 1200,555 L1200,720 L0,720Z" fill="#b8b8b8"/>
  <path d="M0,562 Q600,855 1200,562 L1200,720 L0,720Z" fill="#fff"/>
</svg>
<div class="abs logo" style="left:113px;top:30px"><span class="name">Duskfall</span><span class="sub">VENTURES</span></div>
<nav class="abs nav">
  <a class="active" style="left:0">Home</a>
  <a style="left:84px">Join VC</a>
  <a style="left:180px">Startups</a>
</nav>
<div class="btn" style="left:880px;top:34px;width:152px;height:42px">Get Started <svg viewBox="0 0 22 10"><path d="M0 5H20M16 1L20 5L16 9" stroke="#fff" stroke-width="1.6" fill="none"/></svg></div>
<div class="abs user"><svg viewBox="0 0 43 43" width="43" height="43"><circle cx="21.5" cy="16" r="6" stroke="#111" stroke-width="1.6" fill="none"/><path d="M10 33 Q21.5 20 33 33" stroke="#111" stroke-width="1.6" fill="none"/></svg></div>
<div class="abs hero-moon" role="img" aria-label="Full moon"></div>
<h1 class="abs hero-title"><em>Venture Capital</em> For The<br>Late Night Hustlers</h1>
<div class="abs hero-sub">Become a Venture Capital Investor</div>
<div class="btn" style="left:115px;top:401px;width:153px;height:42px">Learn More <svg viewBox="0 0 22 10"><path d="M0 5H20M16 1L20 5L16 9" stroke="#fff" stroke-width="1.6" fill="none"/></svg></div>
<div class="abs scroll-dot"></div>

<!-- ABOUT -->
<div class="abs moon-big" role="img" aria-label="Detailed photograph of the moon"></div>
<h2 class="abs about-title">Simplifying <b>Success</b><br><b>For Founders</b></h2>
<div class="divider" style="left:651px;top:962px;width:225px"><i style="left:0"></i><span style="left:104px"></span><i style="left:140px"></i></div>
<div class="abs about-text">
  <p>Our strength lies in our network. Our LPs and operating partners are all mid-to-senior level executives in their industries. They bring real-world corporate experience, offering strategic insights and operational support to help our portfolio companies scale efficiently.</p>
  <p>We cut through the noise and get to the core of your business fast. If we love what you’re building, we’ll move. If not, we’ll tell you quickly and respectfully. That lets you make</p>
</div>
<div class="btn" style="left:648px;top:1332px;width:153px;height:43px">Learn More <svg viewBox="0 0 22 10"><path d="M0 5H20M16 1L20 5L16 9" stroke="#fff" stroke-width="1.6" fill="none"/></svg></div>

<!-- FUND ECONOMICS -->
<h2 class="sec-title" style="top:1470px">Fund <b>Economics</b></h2>
<div class="divider" style="left:489px;top:1548px;width:222px"><i style="left:0"></i><span style="left:104px"></span><i style="left:137px"></i></div>
<div class="stat" style="left:112px"><div class="num">14</div><hr><div class="lab">Pre-Seed / Seed<br>Investments</div></div>
<div class="stat" style="left:310px"><div class="num">50K</div><hr><div class="lab">Check Size</div></div>
<div class="stat" style="left:507px"><div class="num">20%</div><hr><div class="lab">Carried Interest</div></div>
<div class="stat" style="left:705px"><div class="num">2.5%</div><hr><div class="lab">Management<br>Fee</div></div>
<div class="stat" style="left:903px"><div class="num">1M</div><hr><div class="lab">Fund Size</div></div>

<!-- BECOME A VC -->
<div class="abs vc-band" role="img" aria-label="Dark lunar surface texture"></div>
<h2 class="sec-title vc-title" style="top:2009px">Become <b>a VC</b></h2>
<div class="divider" style="left:489px;top:2082px;width:222px"><i style="left:0"></i><span style="left:104px"></span><i style="left:137px"></i></div>
<p class="abs vc-lead">At Duskfall Ventures, we’re opening the doors to a new kind of investor, mid-career professionals and aspiring<br>VCs who want real skin in the game, not just exposure from the sidelines.</p>

<div class="vc-card" style="left:112px">
  <div class="img" role="img" aria-label="Professionals working late in a glass office overlooking city lights" style="background:linear-gradient(160deg,#1a3d5c,#2f86b4 45%,#0b1a2a)"></div>
  <h3>Hands on VC Work</h3>
  <p>Each Duskfall Investor can actively be involved in sourcing, evaluating, and making key investment</p>
  <svg class="go" viewBox="0 0 40 40"><circle cx="20" cy="20" r="18" fill="none" stroke="#111" stroke-width="2"/><path d="M11 20H28M23 15L28 20L23 25" stroke="#111" stroke-width="2" fill="none"/></svg>
</div>
<div class="vc-card dark" style="left:443px">
  <div class="img" role="img" aria-label="Golden key resting on a glowing circuit board" style="background:linear-gradient(150deg,#2a1e10,#a7742e 50%,#1a130b)"></div>
  <h3>Earn Carry and Put Your Name on an Investment</h3>
  <p>Earn carry interest based on the level of your involvement on each deal.</p>
  <svg class="go" viewBox="0 0 40 40"><circle cx="20" cy="20" r="18" fill="none" stroke="#fff" stroke-width="2"/><path d="M11 20H28M23 15L28 20L23 25" stroke="#fff" stroke-width="2" fill="none"/></svg>
</div>
<div class="vc-card" style="left:773px">
  <div class="img" role="img" aria-label="Magnifying glass highlighting a yellow house among grey houses" style="background:radial-gradient(circle at 48% 45%,#e0b72a 0 14%,#6a6a6a 30%,#3a3a3a)"></div>
  <h3>Join a community<br>of Hustlers</h3>
  <p>Network with likeminded investors, aspiring investors and limited partners</p>
  <svg class="go" viewBox="0 0 40 40"><circle cx="20" cy="20" r="18" fill="none" stroke="#111" stroke-width="2"/><path d="M11 20H28M23 15L28 20L23 25" stroke="#111" stroke-width="2" fill="none"/></svg>
</div>
<svg class="slide-arrow" style="left:50px" viewBox="0 0 42 42"><circle cx="21" cy="21" r="19" fill="none" stroke="#fff" stroke-width="2"/><path d="M31 21H12M17 15L11 21L17 27" stroke="#fff" stroke-width="2" fill="none"/></svg>
<svg class="slide-arrow" style="left:1101px" viewBox="0 0 42 42"><circle cx="21" cy="21" r="19" fill="none" stroke="#fff" stroke-width="2"/><path d="M11 21H30M25 15L31 21L25 27" stroke="#fff" stroke-width="2" fill="none"/></svg>

<!-- PARTNERS -->
<h2 class="sec-title" style="top:2824px">Our <b>Partners</b></h2>
<div class="divider" style="left:489px;top:2901px;width:222px"><i style="left:0"></i><span style="left:104px"></span><i style="left:137px"></i></div>
<div class="partner" style="left:112px"><span></span></div>
<div class="partner" style="left:360px"><span></span></div>
<div class="partner" style="left:608px"><span></span></div>
<div class="partner" style="left:857px"><span></span></div>

<!-- CTA + FOOTER -->
<svg class="abs foot-curve" viewBox="0 0 1200 893" aria-hidden="true">
  <path d="M0,300 Q600,50 1200,300 V893 H0Z" fill="#b8b8b8"/>
  <path d="M0,365 Q600,115 1200,365 V893 H0Z" fill="#000"/>
</svg>
<div class="abs cta"></div>
<h2 class="abs cta-title">Ready to start <b>investing as a VC?</b></h2>
<div class="divider" style="left:489px;top:3350px;width:222px"><i style="left:0;background:#fff"></i><span style="left:104px;border-color:#fff"></span><i style="left:137px;background:#fff"></i></div>
<p class="abs cta-text">Book an interview to learn more and see if you qualify.</p>
<div class="btn" style="left:522px;top:3453px;width:154px;height:44px;background:#000">Get Started <svg viewBox="0 0 22 10"><path d="M0 5H20M16 1L20 5L16 9" stroke="#fff" stroke-width="1.6" fill="none"/></svg></div>

<div class="abs logo" style="left:112px;top:3650px"><span class="name">Duskfall</span><span class="sub">VENTURES</span></div>
<div class="abs foot-txt" style="left:112px;top:3762px;font-weight:600">Follow Us On:</div>
<span class="social" style="left:108px"></span>
<span class="social" style="left:147px"></span>
<span class="social" style="left:184px"></span>

<div class="abs foot-h" style="left:423px;top:3650px">Contact Us</div>
<div class="abs foot-line" style="left:423px;top:3688px"></div>
<svg class="abs" style="left:424px;top:3728px" width="20" height="24" viewBox="0 0 20 24"><path d="M10 22C4 15 3 12 3 9a7 7 0 0 1 14 0c0 3-1 6-7 13Z" fill="none" stroke="#fff" stroke-width="1.5"/><circle cx="10" cy="9" r="2.5" fill="none" stroke="#fff" stroke-width="1.5"/></svg>
<div class="abs foot-txt" style="left:463px;top:3715px">214 Larkmoor Ave<br>Brightwater, CA 90417</div>
<svg class="abs" style="left:424px;top:3786px" width="22" height="22" viewBox="0 0 22 22"><path d="M4 2l4 1 1 5-2 2a12 12 0 0 0 5 5l2-2 5 1 1 4c-1 2-3 3-5 2C9 18 4 13 2 7 1 5 2 3 4 2Z" fill="none" stroke="#fff" stroke-width="1.5"/></svg>
<div class="abs foot-txt" style="left:463px;top:3784px">123-456-7890</div>
<svg class="abs" style="left:424px;top:3836px" width="22" height="16" viewBox="0 0 22 16"><rect x="1" y="1" width="20" height="14" fill="none" stroke="#fff" stroke-width="1.5"/><path d="M1 1l10 8 10-8" fill="none" stroke="#fff" stroke-width="1.5"/></svg>
<div class="abs foot-txt" style="left:463px;top:3832px">hello@duskfall.example</div>

<div class="abs foot-h" style="left:725px;top:3650px">Subscribe to Our Newsletter</div>
<div class="abs foot-line" style="left:725px;top:3688px"></div>
<div class="abs foot-txt" style="left:727px;top:3715px;font-size:15px;font-weight:600">Email*</div>
<div class="abs input"><svg style="position:absolute;left:279px;top:0" width="59" height="53" viewBox="0 0 59 53"><line x1="0" y1="8" x2="0" y2="45" stroke="#ccc"/><path d="M19 27L41 17L33 38L29 29Z M29 29L41 17" fill="none" stroke="#111" stroke-width="1.5"/></svg></div>
<div class="abs check"></div>
<div class="abs foot-txt" style="left:760px;top:3831px;font-size:15px;font-weight:600">Yes, subscribe me to your newsletter.*</div>

<p class="abs copy">copyright 2025. Company Name. all rights reserved</p>
</body>
</html>
```